Bakery looking for new Business cards

I have a new logo and now its time to upgrade our business cards.
e-mail - info@corwelbakehouse.com
www.corwelbakehouse.com
318-547-2096

418e Pell Creek rd. Marlow Heights IL 60291
Bakery Hour's Tuesday-Saturday 8am-5pm

Industry/Entity Type

Bakery

Contact Information for Business Card

Hr's

Requirements
Must have
• Business information.
Nice to have
• would like to include a QR code for our website.

```html
<!DOCTYPE html>
<html lang="en">
<head>
<meta charset="utf-8">
<title>Corwel Bakehouse – Business Cards</title>
<link href="https://fonts.googleapis.com/css2?family=Oswald:wght@500;600&display=swap" rel="stylesheet">
<style>
  :root {
    --gold: #e2a544;
    --white: #ffffff;
    --ink: #1c1c1c;
    --backdrop: #f1ebe2;
  }
  * { margin: 0; padding: 0; box-sizing: border-box; }
  html, body { width: 1200px; height: 855px; overflow: hidden; }
  body {
    background: var(--backdrop);
    font-family: "Oswald", "Arial Narrow", sans-serif;
    position: relative;
  }
  .card {
    position: absolute;
    width: 429px;
    height: 236px;
    overflow: hidden;
    box-shadow: 0 6px 14px rgba(0,0,0,0.22);
  }
  /* Front */
  .card-front { left: 153px; top: 327px; background: var(--gold); }
  .card-front .frame {
    position: absolute; inset: 17px 14px 11px 18px;
    border: 2px solid var(--white);
  }
  .card-front .badge {
    position: absolute; left: 90px; top: -7px;
    width: 248px; height: 248px; border-radius: 50%;
    background: var(--white);
    display: flex; align-items: center; justify-content: center;
  }
  .brand-name {
    color: var(--ink);
    font-weight: 600;
    letter-spacing: 0.5px;
    white-space: nowrap;
  }
  .card-front .brand-name { font-size: 30px; }
  /* Back */
  .card-back { left: 599px; top: 330px; background: var(--white); }
  .card-back .brand-side {
    position: absolute; left: 0; top: 0; width: 190px; height: 100%;
    display: flex; align-items: center; justify-content: center;
  }
  .card-back .brand-name { font-size: 21px; }
  .card-back .info-panel {
    position: absolute; left: 190px; top: 0; right: 0; bottom: 0;
    background: var(--gold);
  }
  .info-panel .frame-top {
    position: absolute; left: 0; right: 16px; top: 17px; height: 2px;
    background: var(--white);
  }
  .info-panel .frame-right {
    position: absolute; right: 16px; top: 17px; width: 2px; height: 179px;
    background: var(--white);
  }
  .info-panel .hours-band {
    position: absolute; left: 0; right: 0; top: 196px; height: 29px;
    background: var(--white);
    display: flex; align-items: center; justify-content: center;
  }
  .hours {
    color: var(--gold); font-size: 13px; font-weight: 600;
    white-space: nowrap;
  }
  .contact-list { list-style: none; position: absolute; left: 14px; top: 53px; }
  .contact-list li {
    display: flex; align-items: flex-start; gap: 11px;
    color: var(--white); font-size: 15px; font-weight: 500;
    line-height: 19px; margin-bottom: 8px; white-space: nowrap;
  }
  .contact-list li.address { margin-top: 15px; }
  .icon {
    width: 17px; height: 17px; border-radius: 50%;
    background: var(--ink); flex: none; margin-top: 1px;
    display: flex; align-items: center; justify-content: center;
  }
  .icon svg { width: 10px; height: 10px; }
</style>
</head>
<body>
  <section class="card card-front">
    <div class="frame"></div>
    <div class="badge">
      <span class="brand-name">Corwel Bakehouse</span>
    </div>
  </section>

  <section class="card card-back">
    <div class="brand-side">
      <span class="brand-name">Corwel Bakehouse</span>
    </div>
    <div class="info-panel">
      <div class="frame-top"></div>
      <div class="frame-right"></div>
      <ul class="contact-list">
        <li>
          <span class="icon"><svg viewBox="0 0 10 10"><rect x="1" y="2.5" width="8" height="5.5" fill="none" stroke="#fff" stroke-width="1"/><path d="M1 2.5 L5 5.8 L9 2.5" fill="none" stroke="#fff" stroke-width="1"/></svg></span>
          info@corwelbakehouse.com
        </li>
        <li>
          <span class="icon"><svg viewBox="0 0 10 10"><circle cx="5" cy="5" r="4" fill="none" stroke="#fff" stroke-width="0.9"/><ellipse cx="5" cy="5" rx="1.8" ry="4" fill="none" stroke="#fff" stroke-width="0.8"/><path d="M1 5 H9 M1.7 3 H8.3 M1.7 7 H8.3" stroke="#fff" stroke-width="0.7"/></svg></span>
          www.corwelbakehouse.com
        </li>
        <li>
          <span class="icon"><svg viewBox="0 0 10 10"><path d="M2.2 1.2 L3.8 1 L4.6 3.1 L3.6 4 Q4.5 5.8 6 6.5 L6.9 5.4 L9 6.2 L8.8 7.8 Q7.8 9 6 8.4 Q2.5 7 1.4 3.6 Q1 2 2.2 1.2 Z" fill="#fff"/></svg></span>
          318-547-2096
        </li>
        <li class="address">
          <span class="icon"><svg viewBox="0 0 10 10"><path d="M5 9.4 L2.3 5.6 A3.2 3.2 0 1 1 7.7 5.6 Z" fill="#fff"/><circle cx="5" cy="3.8" r="1.2" fill="#1c1c1c"/></svg></span>
          <span>418e Pell Creek rd.<br>Marlow Heights IL 60291</span>
        </li>
      </ul>
      <div class="hours-band">
        <span class="hours">Bakery Hour's Tuesday- Saturday 8am-5pm</span>
      </div>
    </div>
  </section>
</body>
</html>
```